Torqline general brochure

we are family owned and run industrial bearing and power transmission company. i have attached our own "home made" brochure but need something more proffessional looking to use as a first point of call and also as a guide to what we supply and are capable of...

Target Market(s)

purchasing officers, maintenance staff

Industry/Entity Type

Industrial

Requirements
Must have
• must have all logos
both company locations but the Cobalt Lake ine is the main warehouse and head office
Nice to have
• this really needs to be broad, we want people to know what we can supply and something which looks more than a home made, cheap attempt..

```html
<!DOCTYPE html>
<html lang="en">
<head>
<meta charset="utf-8">
<title>Torqline brochure – inside spread</title>
<link href="https://fonts.googleapis.com/css2?family=Roboto:wght@300;400;700&family=Roboto+Condensed:wght@400;700&display=swap" rel="stylesheet">
<style>
:root{
  --orange:#ff5a12;
  --orange-light:#ff7a30;
  --ink:#222;
  --charcoal:#3a3a3a;
  --paper:#fff;
}
*{margin:0;padding:0;box-sizing:border-box}
html,body{width:1200px;height:1000px;overflow:hidden;background:#fff}
body{position:relative;font-family:"Roboto",Arial,sans-serif;color:var(--ink)}
.spread{position:absolute;left:33px;top:57px;width:1135px;height:803px;
  background:linear-gradient(180deg,var(--orange) 0%,var(--orange-light) 50%,var(--orange) 100%);
  box-shadow:0 4px 6px rgba(0,0,0,.45)}
.gutter{position:absolute;left:520px;top:0;width:110px;height:100%;
  background:linear-gradient(90deg,rgba(0,0,0,0) 0%,rgba(0,0,0,.08) 45%,rgba(0,0,0,.45) 51%,rgba(255,255,255,.18) 56%,rgba(0,0,0,0) 100%)}
.page-panel{position:absolute;top:53px;height:695px;background:var(--paper)}
.panel-left{left:0;width:519px;border-radius:0 22px 22px 0}
.panel-right{left:615px;width:520px;border-radius:22px 0 0 22px}
.tag{position:absolute;left:0;color:#fff;font-family:"Roboto Condensed",Arial,sans-serif;font-weight:700}
.tag-about{top:18px;width:299px;height:34px;background:var(--orange);font-size:19px;line-height:34px;padding-left:90px;
  clip-path:polygon(0 0,288px 0,299px 50%,288px 100%,0 100%)}
.tag-service{top:421px;width:485px;height:33px;background:var(--charcoal);font-size:13px;line-height:33px;padding-left:91px;
  clip-path:polygon(0 0,475px 0,485px 50%,475px 100%,0 100%)}
.about{position:absolute;left:91px;top:71px;width:390px;font-size:11px;line-height:15px;font-weight:300;letter-spacing:.25px;color:#111}
.about p{margin-bottom:11px}
.community{position:absolute;left:91px;top:478px;font-size:11px;font-weight:300;letter-spacing:.2px;color:#111}
.community h3{font-size:10.5px;font-weight:700;letter-spacing:0;margin-bottom:13px}
.community li{list-style:none;display:flex;align-items:center;gap:6px;height:26px}
.community svg{width:16px;height:16px}
.col{position:absolute;left:658px;top:79px;font-size:10.5px;line-height:14.8px;font-weight:300;letter-spacing:.25px;color:#111}
.col h4{color:var(--orange);font-weight:700;font-size:11px;letter-spacing:.2px;margin-bottom:10px}
.col h4.next{margin:11px 0 0}
.col ul{list-style:none}
.col li::before{content:"• "}
.photo{position:absolute;border-radius:10px;width:93px;height:63px}
.round{position:absolute;border-radius:50%}
.wide-photo{position:absolute;left:658px;top:659px;width:423px;height:68px;border-radius:10px;
  background:linear-gradient(90deg,#6d6a62,#a8a49a 35%,#4c4a46 70%,#8d8a83)}
.label{position:absolute;top:877px;font-family:"Roboto Condensed",Arial,sans-serif;font-size:24px;color:#111;transform:translateX(-50%)}
</style>
</head>
<body>
<section class="spread">
  <div class="gutter"></div>

  <div class="page-panel panel-left">
    <h2 class="tag tag-about">About Torqline</h2>
    <div class="about">
      <p>Torqline is locally owned and operated company with branches strategically located in Cobalt Lake and Wendell Park - Port Ardent - Western Coast.</p>
      <p>Founded in 2001, Torqline has cemented itself as a well recognised and regarded supplier of quality bearings, electric motors, industrial gearboxes and power transmission supplies. With a proud history of reliability and unparalleled customer service, Torqline have accepted distribution opportunities from world leading manufacturers such as Kelvar, Beltrix, Vorn, Castellano, Rakova, Lockfast, Motoriva, Lemont Sorel and Dunmore.</p>
      <p>Understanding that good old fashioned customer service, quality products and local stock availability are often difficult to find, Torqline continue to expand their stock holdings and remain passionate and committed to servicing existing and<br>new customers.</p>
      <p>Having identified a need for not only supply, Torqline have recently moved ino the area of on site servicing and related services, giving the ability to offer a complete package.</p>
      <p>Contact us today to discuss your requirements.</p>
    </div>
    <h2 class="tag tag-service">Torqline - Bearing and Power Transmission - Supply <em>and Service</em></h2>
    <div class="community">
      <h3>Torqline is a Community Conscious Company Proudly supporting:</h3>
      <ul>
        <li><svg viewBox="0 0 16 16"><circle cx="8" cy="8" r="7" fill="var(--orange)"/><circle cx="8" cy="8" r="2.5" fill="#fff"/></svg>Nova Calisthenics</li>
        <li><svg viewBox="0 0 16 16"><circle cx="8" cy="8" r="7" fill="var(--orange)"/><circle cx="8" cy="8" r="2.5" fill="#fff"/></svg>Harbourside Hawks Masters</li>
        <li><svg viewBox="0 0 16 16"><circle cx="8" cy="8" r="7" fill="var(--orange)"/><circle cx="8" cy="8" r="2.5" fill="#fff"/></svg>Hillcrest Rugby Union</li>
        <li><svg viewBox="0 0 16 16"><circle cx="8" cy="8" r="7" fill="var(--orange)"/><circle cx="8" cy="8" r="2.5" fill="#fff"/></svg>Bayview Junior Football</li>
        <li><svg viewBox="0 0 16 16"><circle cx="8" cy="8" r="7" fill="var(--orange)"/><circle cx="8" cy="8" r="2.5" fill="#fff"/></svg>Global Hope Aid</li>
      </ul>
    </div>
  </div>

  <div class="page-panel panel-right"></div>

  <div class="col">
    <h4>AUTHORISED DISTRIBUTOR</h4>
    <ul>
      <li>Bearings</li><li>Housings</li><li>Power Transmission</li><li>Seals</li><li>Mechatronics</li><li>Services</li><li>Chains and sprockets</li><li>Lip Seals</li><li>Shaft couplings</li><li>Grid &amp; Gear couplings</li><li>Tyre couplings</li><li>Spacer couplings</li><li>Jaw couplings</li><li>Disco flex couplings</li><li>Wedge and vee belts</li><li>Banded belts</li><li>HTD and timing belts</li><li>Multi-rib and link belts</li><li>Vee and HTD pulleys</li><li>Taper bushes</li><li>Locking assemblies</li><li>Rolvex Conveyor components</li><li>Vorn Electric motors</li>
    </ul>
    <h4 class="next">GEARBOXES</h4>
    <ul><li>Inline helical</li><li>Worm boxes</li><li>Bevel Helical</li><li>Planetary</li><li>Shaft mounted</li></ul>
    <h4 class="next">AGENTS FOR:</h4>
    <ul><li>Castellano</li><li>Motoriva</li><li>Lemont Sorel</li><li>Dunmore</li></ul>
  </div>

  <div class="round" role="img" aria-label="Seal and coupling parts" style="left:834px;top:144px;width:62px;height:62px;background:radial-gradient(#3a7bd5,#cfe6f5)"></div>
  <div class="round" role="img" aria-label="Jaw coupling spiders" style="left:814px;top:255px;width:76px;height:76px;background:radial-gradient(#2b2b2b,#d8d8d8)"></div>
  <div class="round" role="img" aria-label="Tyre coupling element" style="left:816px;top:442px;width:58px;height:58px;background:radial-gradient(#1c1c1c,#e0e0e0)"></div>
  <div class="round" role="img" aria-label="Chain sprockets" style="left:758px;top:518px;width:102px;height:102px;background:radial-gradient(#3b3b3b,#c9c9c9)"></div>

  <div class="photo" role="img" aria-label="Plummer block bearing housing" style="left:885px;top:81px;background:linear-gradient(#7fd3ea,#1c3f7a)"></div>
  <div class="photo" role="img" aria-label="Roller bearing" style="left:988px;top:81px;background:linear-gradient(#bfeaf6,#5a6570)"></div>
  <div class="photo" role="img" aria-label="Pillow block bearing" style="left:885px;top:151px;background:linear-gradient(#8fd8ee,#2a4f9a)"></div>
  <div class="photo" role="img" aria-label="Oil seals" style="left:988px;top:151px;background:linear-gradient(#a8e2f3,#3a3f45)"></div>
  <div class="photo" role="img" aria-label="Grid coupling" style="left:885px;top:222px;background:linear-gradient(#7fd3ea,#545b60)"></div>
  <div class="photo" role="img" aria-label="Timing belt" style="left:988px;top:222px;background:linear-gradient(#9adcf0,#b0203a)"></div>
  <div class="photo" role="img" aria-label="Banded vee belts" style="left:885px;top:292px;background:linear-gradient(#7fd3ea,#2d6fc0)"></div>
  <div class="photo" role="img" aria-label="Vee belt pulley" style="left:988px;top:292px;background:linear-gradient(#a8e2f3,#2b2b2b)"></div>
  <div class="photo" role="img" aria-label="Inline helical gearbox" style="left:885px;top:363px;background:linear-gradient(#5cc6e8,#1a5a9c)"></div>
  <div class="photo" role="img" aria-label="Shaft mounted gearbox" style="left:988px;top:363px;background:linear-gradient(#7fd3ea,#2a6aaa)"></div>
  <div class="photo" role="img" aria-label="Blue worm gearbox with motor" style="left:885px;top:434px;border:1px solid #333;background:linear-gradient(#fff,#2a5fa8)"></div>
  <div class="photo" role="img" aria-label="Bevel helical gearbox" style="left:988px;top:434px;background:linear-gradient(#6fcfee,#3d78c0)"></div>
  <div class="photo" role="img" aria-label="White planetary gearbox" style="left:885px;top:505px;background:linear-gradient(#5cc6e8,#d9eef6)"></div>
  <div class="photo" role="img" aria-label="Blue helical gearmotor" style="left:988px;top:505px;border:1px solid #333;background:linear-gradient(#fff,#2a5fa8)"></div>
  <div class="photo" role="img" aria-label="Worm gearbox" style="left:885px;top:575px;border:1px solid #333;background:linear-gradient(#e8eef4,#1e4f9c)"></div>
  <div class="photo" role="img" aria-label="Conveyor rollers" style="left:988px;top:575px;background:linear-gradient(#6a5f7a,#3a4fa8)"></div>

  <div class="wide-photo" role="img" aria-label="Technician servicing equipment on site"></div>
</section>

<p class="label" style="left:279px">Inside Left</p>
<p class="label" style="left:901px">Inside Right</p>
</body>
</html>
```